Hollis Ironworks Business Card

We need a business card design for a new small metal fabrication business in rural NSW, Australia.

The business (Hollis Ironworks) is owner operated by a man with the initials RB - much of the branding comes from this name.

Hollis Ironworks designs, engineers, repairs and manufactures a range of custom, quality metal works including vehicle trays, agricultural machinery impliments, trailers, wood splitters, fire pits, furniture etc.

The brand position focuses on custom work of the highest quality.

Business card design should show quality, attention to detail and stand out among a mass of business cards.

Logos are in the files

The grey color may be changed on the logo if required to stand out more.

There is an image attached of a simple card that is liked because it is clean, clear, simple, masculine and effective. It says 'quality'. As most of the work we do is custom it would be good to have the business card speak to this.

Target Market(s)

Rural and regional based Australians. Primarily adult male 25-60 yrs. Primary production / rural / travelling lifestyle.

Industry/Entity Type

Metal Fabrication

Contact Information for Business Card

The words 'custom quality fabrications' would be great somewhere perhaps on the backside (not on the information side)
Name
title
Phone: 0491 538 274 and (02) 7342 9185
email: info@hollisiw.com.au
www.hollisiw.com.au

address (2 lines)

Requirements
Nice to have
• Background colour should be very navy blue or black.
Should not have
• NO orange and blue combinations.
• Navy is OK

```html
<!DOCTYPE html>
<html lang="en">
<head>
<meta charset="utf-8">
<title>Hollis Ironworks Business Card</title>
<link href="https://fonts.googleapis.com/css2?family=Questrial&display=swap" rel="stylesheet">
<style>
  :root {
    --backdrop: #2b2b2b;
    --card-light: #f7f7f7;
    --card-dark: #1b1b1b;
    --brand-green: #62b83e;
    --brand-grey: #8e8e8e;
    --text-dark: #2a2a2a;
    --text-mid: #555555;
    --text-light: #d8d8d8;
  }
  * { margin: 0; padding: 0; box-sizing: border-box; }
  html, body {
    width: 1200px; height: 516px; overflow: hidden;
    background: var(--backdrop);
    font-family: "Questrial", "Century Gothic", sans-serif;
  }
  .stage { position: relative; width: 1200px; height: 516px; }
  .card {
    position: absolute; top: 123px; width: 454px; height: 280px;
    box-shadow: 0 4px 14px rgba(0,0,0,0.45);
    overflow: hidden;
  }
  .card--front { left: 129px; background: var(--card-light); }
  .card--back { left: 602px; background: var(--card-dark); }

  .brand { position: absolute; display: flex; align-items: center; gap: 8px; }
  .brand__mark { width: 16px; height: 16px; background: var(--brand-green); }
  .brand__name {
    font-size: 22px; letter-spacing: 1.5px; text-transform: uppercase;
    color: var(--brand-grey); line-height: 1;
  }
  .card--front .brand { left: 26px; top: 50px; }
  .card--back .brand { right: 36px; top: 208px; }
  .card--back .brand__name { font-size: 18px; color: var(--text-light); }

  .person { position: absolute; left: 31px; top: 125px; }
  .person__name { font-size: 14.5px; color: var(--brand-green); line-height: 18px; }
  .person__title { font-size: 10.5px; color: var(--text-mid); line-height: 14px; }

  .address {
    position: absolute; left: 31px; top: 165px;
    font-size: 12.5px; line-height: 15px; color: var(--text-dark); font-style: normal;
  }
  .contacts { position: absolute; left: 31px; top: 205px; list-style: none; }
  .contacts li {
    display: flex; align-items: center; gap: 4px;
    font-size: 12.5px; line-height: 15.5px; color: var(--text-dark);
  }
  .contacts svg { width: 10px; height: 10px; flex: none; }

  .tagline {
    position: absolute; right: 33px; top: 232px;
    font-size: 13px; color: var(--brand-green);
  }
</style>
</head>
<body>
<main class="stage">
  <section class="card card--front" aria-label="Card front">
    <div class="brand">
      <span class="brand__mark"></span>
      <span class="brand__name">Hollis Ironworks</span>
    </div>
    <div class="person">
      <p class="person__name">Employee Name</p>
      <p class="person__title">Owner</p>
    </div>
    <address class="address">88 Forge Road Drive,<br>Glenbrook, NSW 2799</address>
    <ul class="contacts">
      <li>
        <svg viewBox="0 0 10 10" aria-hidden="true"><rect x="2.5" y="0.5" width="5" height="9" rx="1" fill="none" stroke="#62b83e" stroke-width="1.2"/></svg>
        0491 538 274
      </li>
      <li>
        <svg viewBox="0 0 10 10" aria-hidden="true"><rect width="10" height="10" rx="2" fill="#62b83e"/><path d="M3 2.5 L4.3 2.5 L4.8 4 L4 4.6 Q4.8 6 6 6.6 L6.6 5.8 L8 6.3 L8 7.5 Q5.5 8 3.5 5.5 Q2.5 4 3 2.5Z" fill="#fff"/></svg>
        (02) 7342 9185
      </li>
      <li>
        <svg viewBox="0 0 10 10" aria-hidden="true"><rect x="0.5" y="2" width="9" height="6.5" fill="#62b83e"/><path d="M0.5 2 L5 5.5 L9.5 2" fill="none" stroke="#fff" stroke-width="0.9"/></svg>
        info@hollisiw.com.au
      </li>
      <li>
        <svg viewBox="0 0 10 10" aria-hidden="true"><g fill="none" stroke="#62b83e" stroke-width="0.9"><circle cx="5" cy="5" r="4.3"/><ellipse cx="5" cy="5" rx="2" ry="4.3"/><path d="M0.7 5 H9.3"/></g></svg>
        www.hollisiw.com.au
      </li>
    </ul>
  </section>

  <section class="card card--back" aria-label="Card back">
    <div class="brand">
      <span class="brand__mark"></span>
      <span class="brand__name">Hollis Ironworks</span>
    </div>
    <p class="tagline">Custom Quality Fabrications</p>
  </section>
</main>
</body>
</html>
```